Design BRVMentoring.com

Looking to build a business professional coach website arround Vendrixo.com , it will some standard pages, about me, a page or 2 on vendrixo, maybe with a download and email grab, contact me....

```html
<!DOCTYPE html>
<html lang="en">
<head>
<meta charset="utf-8">
<title>BRV Mentoring</title>
<link href="https://fonts.googleapis.com/css2?family=Outfit:wght@300;400;500;600;700&display=swap" rel="stylesheet">
<style>
:root{
  --green:#8dc21f;
  --purple:#4b2085;
  --blue:#1a8ad4;
  --orange:#f5a300;
  --brown:#8d6330;
  --dark:#1d1d1d;
  --grey:#5b5353;
  --text:#555;
  --paper:#f8f7f5;
  --white:#fff;
}
*{margin:0;padding:0;box-sizing:border-box}
html,body{width:1200px;height:3401px;overflow:hidden}
body{position:relative;background:var(--paper);font-family:'Outfit',sans-serif;color:var(--text)}
.abs{position:absolute}
.header{left:0;top:0;width:1200px;height:87px;background:var(--white)}
.brand{left:26px;top:28px;display:flex;align-items:center;gap:10px}
.brand-dot{width:40px;height:40px;border-radius:50%;background:var(--green)}
.brand-name{font-size:22px;font-weight:600;color:var(--purple);letter-spacing:.5px}
.nav a{position:absolute;top:33px;height:33px;line-height:33px;font-size:14px;font-weight:500;color:#444;text-decoration:none;text-transform:uppercase}
.nav .active{background:var(--green);color:#fff;border-radius:4px;width:112px;text-align:center}
.btn{display:flex;align-items:center;justify-content:center;gap:6px;background:var(--green);color:#fff;font-weight:600;font-size:13px;text-transform:uppercase;border-radius:3px}
.btn .arr{width:12px;height:12px;border-radius:50%;background:#fff;position:relative}
.btn .arr::after{content:"";position:absolute;left:3px;top:3px;border-left:6px solid var(--green);border-top:3px solid transparent;border-bottom:3px solid transparent}
.hero{left:0;top:87px;width:1200px;height:560px;background:linear-gradient(100deg,#f6a04d33 0%,#eef0f4 30%,#dfe6ef 60%,#b6ddf2 100%)}
.hero-deco-l{left:0;top:87px;width:420px;height:360px;background:radial-gradient(ellipse at 30% 20%,#f26b4f66,#f9b24f44 40%,transparent 70%)}
.hero-deco-r{left:880px;top:250px;width:320px;height:397px;background:radial-gradient(ellipse at 60% 50%,#f7d23c66,#7a4fb044 45%,transparent 75%)}
.hero-photo{left:673px;top:120px;width:291px;height:527px;background:linear-gradient(180deg,#d9c7bb,#2a2a2d 60%);border-radius:140px 140px 0 0}
.hero h1{left:32px;top:268px;font-size:43px;font-weight:600;color:var(--dark)}
.hero-list{left:30px;top:338px;font-size:26px;color:var(--dark);font-weight:400;line-height:41px;list-style:none}
.hero-list li::before{content:"✓";color:var(--blue);font-size:16px;margin-right:8px;vertical-align:middle}
.about-pic{left:105px;top:735px;width:410px;height:375px}
.eyebrow{font-size:17px;font-weight:500;color:var(--brown)}
.h2{font-size:27px;font-weight:600;color:var(--blue)}
.h2 span{color:var(--orange)}
.para{font-size:12.5px;line-height:19px;text-align:justify;color:#444}
.cards .card{position:absolute;top:1175px;width:268px;height:101px;border-radius:4px 4px 10px 10px;display:flex;align-items:center;gap:14px;padding-left:12px;color:#fff;font-size:20px;font-weight:500}
.card .ico{width:78px;height:78px;border-radius:50%;background:#fff;display:flex;align-items:center;justify-content:center}
.card .ico i{width:30px;height:30px;border-radius:50%}
.services{left:0;top:1320px;width:1200px;height:925px;background:#fff}
.center-copy{left:415px;top:1770px;width:370px;text-align:center;font-size:13px;line-height:19px;color:#555}
.node-label{position:absolute;width:140px;text-align:center;color:#fff;font-size:16px;font-weight:500;line-height:24px}
.form{left:647px;top:2333px;width:506px;height:389px;border:2px solid var(--purple);border-radius:8px;background:#fff}
.form label{position:absolute;left:20px;font-size:11px;font-weight:600;color:#333}
.form .field{position:absolute;left:20px;width:464px;height:30px;border:1px solid #aaa;border-radius:3px;font-size:11px;color:#888;padding:7px 12px}
.contact-item{display:flex;gap:14px}
.contact-item b{display:block;font-size:15px;font-weight:500;color:#222}
.contact-item small{display:block;font-size:12px;color:#444;margin-top:10px}
.footer-links a{color:#fff;text-decoration:none;font-size:14px;margin:0 14px}
.social{width:38px;height:38px;border-radius:50%;border:2px solid var(--purple);background:#fff}
</style>
</head>
<body>

<header class="abs header">
  <div class="abs brand"><div class="brand-dot"></div><div class="brand-name">BRV MENTORING</div></div>
  <nav class="nav">
    <a class="active" style="left:337px">Home</a>
    <a style="left:485px">About Me</a>
    <a style="left:627px">Services</a>
    <a style="left:763px">Contact</a>
  </nav>
  <div class="abs btn" style="left:997px;top:33px;width:163px;height:44px">Contact Me <span class="arr"></span></div>
</header>

<section class="abs hero"></section>
<div class="abs hero-deco-l"></div>
<div class="abs hero-deco-r"></div>
<div class="abs hero-photo" role="img" aria-label="Photo of a smiling businesswoman in a dark suit and glasses"></div>
<div class="hero">
  <h1 class="abs" style="left:32px;top:268px;font-size:43px;font-weight:600;color:var(--dark)">Welcome To BRV Mentoring</h1>
  <ul class="abs hero-list">
    <li>Your Premier Business Professional Coach</li>
    <li>Elevate Your Career with BRV Mentoring</li>
  </ul>
</div>
<div class="abs btn" style="left:32px;top:431px;width:178px;height:44px">Explore More <span class="arr"></span></div>

<svg class="abs" style="left:100px;top:730px" width="420" height="385" viewBox="0 0 420 385">
  <path d="M50 8 C-30 90 0 330 200 380 C270 385 320 360 360 325" fill="none" stroke="var(--purple)" stroke-width="7" stroke-linecap="round"/>
</svg>
<div class="abs about-pic" role="img" aria-label="Portrait of a businesswoman beside a sketched startup and growth illustration" style="background:linear-gradient(90deg,#3a3335 0%,#cbb9b0 35%,#eef0f2 60%,#f6e7d2 100%);border-radius:0 0 0 200px;opacity:.85"></div>

<div class="abs eyebrow" style="left:608px;top:785px">About Me</div>
<div class="abs h2" style="left:608px;top:818px">Get To Know <span>Your Coach</span></div>
<p class="abs para" style="left:608px;top:870px;width:545px">Hello, and welcome to the world of professional coaching! My name is [Your Name], and I am thrilled to have the opportunity to work with you on your journey to personal and professional growth. Allow me to introduce myself and share a bit about my background, experience, and coaching philosophy.</p>
<div class="abs btn" style="left:975px;top:972px;width:178px;height:44px">Explore More <span class="arr"></span></div>

<div class="cards">
  <div class="card" style="left:28px;background:var(--purple)"><div class="ico"><i style="background:var(--purple)"></i></div>My Background</div>
  <div class="card" style="left:320px;background:var(--orange)"><div class="ico"><i style="background:var(--orange)"></i></div>My Qualifications</div>
  <div class="card" style="left:612px;background:var(--brown)"><div class="ico"><i style="background:var(--brown)"></i></div>My Experience</div>
  <div class="card" style="left:904px;background:var(--blue)"><div class="ico"><i style="background:var(--blue)"></i></div>My Philosophy</div>
</div>

<section class="abs services" style="background:var(--paper)"></section>
<div class="abs eyebrow" style="left:0;top:1372px;width:1200px;text-align:center">Our Coaching Services</div>
<div class="abs h2" style="left:0;top:1405px;width:1200px;text-align:center">Unlock Your Potential With <span>Our Comprehensive Coaching Services</span></div>

<svg class="abs" style="left:0;top:1500px" width="1200" height="740" viewBox="0 1500 1200 740">
  <circle cx="600" cy="1802" r="245" fill="none" stroke="#999" stroke-width="6" stroke-dasharray="0 13" stroke-linecap="round"/>
  <circle cx="600" cy="1802" r="216" fill="#fff" stroke="#9a9a9a" stroke-width="9"/>
  <!-- leadership -->
  <polygon points="362,1777 395,1807 362,1837" fill="var(--purple)"/>
  <circle cx="283" cy="1807" r="79" fill="var(--grey)"/>
  <!-- time -->
  <polygon points="838,1777 805,1807 838,1837" fill="var(--orange)"/>
  <circle cx="916" cy="1807" r="79" fill="var(--orange)"/>
  <circle cx="916" cy="1807" r="70" fill="var(--grey)"/>
  <!-- career -->
  <path d="M375 1953 L453 1953 L453 2031 A78 78 0 1 1 375 1953 Z" fill="var(--green)"/>
  <circle cx="375" cy="2031" r="70" fill="var(--grey)"/>
  <!-- stress -->
  <path d="M824 1953 L746 1953 L746 2031 A78 78 0 1 0 824 1953 Z" fill="var(--blue)"/>
  <circle cx="824" cy="2031" r="70" fill="var(--grey)"/>
  <!-- communication -->
  <path d="M600 2015 L660 2078 A78 78 0 1 1 540 2078 Z" fill="var(--brown)"/>
  <circle cx="600" cy="2124" r="70" fill="var(--grey)"/>
  <g fill="#fff">
    <rect x="270" y="1765" width="26" height="18" rx="2"/>
    <rect x="903" y="1765" width="26" height="20" rx="2"/>
    <rect x="362" y="1988" width="26" height="18" rx="2"/>
    <rect x="811" y="1988" width="26" height="20" rx="2"/>
    <rect x="587" y="2083" width="26" height="18" rx="2"/>
  </g>
</svg>
<p class="abs center-copy">Take your leadership skills to the next level. Our leadership coaching program focuses on enhancing your ability to lead teams, make critical decisions, and drive organizational success.</p>
<div class="node-label" style="left:213px;top:1790px">Leadership<br>Coaching</div>
<div class="node-label" style="left:846px;top:1790px">Time and<br>Productivity</div>
<div class="node-label" style="left:305px;top:2014px">Career<br>Advancement</div>
<div class="node-label" style="left:754px;top:2014px">Stress<br>Management</div>
<div class="node-label" style="left:530px;top:2107px">Effective<br>Communication</div>

<div class="abs eyebrow" style="left:47px;top:2370px">Get In Touch</div>
<div class="abs h2" style="left:47px;top:2403px;width:460px;line-height:33px">Your Path To Success <span>Begins With A Conversation!</span></div>
<p class="abs para" style="left:47px;top:2487px;width:545px">Feel free to reach out to me at any time. I'm here to assist you on your journey towards personal and professional growth. Whether you have questions, need further information, or are ready to schedule a coaching session, I'm just a message away. Let's start your transformation today!</p>
<div class="abs contact-item" style="left:58px;top:2607px">
  <svg width="28" height="22" viewBox="0 0 28 22" style="margin-top:12px"><rect width="28" height="20" rx="2" fill="var(--purple)"/><path d="M1 2 L14 12 L27 2" stroke="#fff" stroke-width="2" fill="none"/></svg>
  <div><b>Email Me</b><small>info@BRVMentoring.com</small></div>
</div>
<div class="abs contact-item" style="left:316px;top:2607px">
  <svg width="26" height="26" viewBox="0 0 24 24" style="margin-top:8px"><path fill="var(--purple)" d="M20 15.5c-1.2 0-2.4-.2-3.6-.6-.3-.1-.7 0-1 .2l-2.2 2.2c-2.8-1.4-5.1-3.8-6.6-6.6l2.2-2.2c.3-.3.4-.7.2-1-.3-1.1-.5-2.3-.5-3.5 0-.6-.4-1-1-1H4c-.6 0-1 .4-1 1 0 9.4 7.6 17 17 17 .6 0 1-.4 1-1v-3.5c0-.6-.4-1-1-1z"/></svg>
  <div><b>Call Me</b><small>+1 555 014 2210</small></div>
</div>

<form class="abs form">
  <label style="top:20px">Name</label><div class="field" style="top:34px">Name</div>
  <label style="top:72px">Phone</label><div class="field" style="top:86px">Phone</div>
  <label style="top:124px">Email</label><div class="field" style="top:138px">Email</div>
  <label style="top:176px">Subject</label><div class="field" style="top:190px">Subject</div>
  <label style="top:228px">Message</label><div class="field" style="top:242px;height:75px">Message</div>
  <div class="abs btn" style="left:20px;top:330px;width:464px;height:43px;font-size:14px">Send Your Message</div>
</form>

<svg class="abs" style="left:0;top:2770px" width="1200" height="631" viewBox="0 0 1200 631">
  <path d="M0 190 C250 110 500 120 700 190 C860 240 1040 90 1180 0 L1200 0 L1200 631 L0 631 Z" fill="var(--green)"/>
  <path d="M0 195 C250 235 500 290 700 255 C900 215 1060 100 1200 35 L1200 631 L0 631 Z" fill="var(--purple)"/>
</svg>
<div class="abs" style="left:0;top:3035px;width:1200px;display:flex;justify-content:center;align-items:center;gap:10px">
  <div style="width:30px;height:30px;border-radius:50%;background:var(--green)"></div>
  <div style="font-size:20px;font-weight:600;color:#fff">BRV MENTORING</div>
</div>
<div class="abs footer-links" style="left:0;top:3132px;width:1200px;text-align:center">
  <a style="color:var(--orange)">Home</a><a>About Me</a><a>Services</a><a>Contact</a>
</div>
<div class="abs" style="left:0;top:3175px;width:1200px;display:flex;justify-content:center;gap:6px">
  <div class="social"></div><div class="social"></div><div class="social"></div>
</div>
<div class="abs" style="left:0;top:3250px;width:1200px;text-align:center;color:#fff;font-size:14px">Copyright © 2023 BRVMentoring | Powered by BRVMentoring</div>

</body>
</html>
```